'Orla Property Development' Business Card

Business Card Features:

High Quality (potentially textured) thick card - preference is white textured card

Logo (supplied)

We plan to use the vertical logo as the main logo. But i am happy for people to use either if they find it works better for the design of the card.

The building icon and also the insert to the 'E' is in a metallic finish, i think this should be finished in a metallic embossed or raised style.
Updates

Please note i have attached both a horizontal and Vertical Logo for your reference. We plan to use the vertical logo as the main logo. But i am happy for people to use either if they find it works better for the design of the card.

Please note i am considering having the cards made on stainless steel. This introduces the option of having cut outs in the card and etching or printing for the design. If you have a good concept for this please submit.

http://www.quorvantprint.co.uk/black-metal-cards# this is a site that makes the metal cards to offer some direction . . . . Please note i am basic the selection o the best design, if that means normal print cards on paper then this is what i will choose. But there are some great options with the metal. Thanks.

Industry/Entity Type

Building

Requirements
Must have
• Helvetica font to details side of card - logo as supplied to opposite side.

Card Details:

Darren Ashcombe
Managing Director

+61 438 615 207
+61 3 8276 4139

PO Box 73
Marrowfield, VIC 3291

darren@orla.properties

www.orla.properties

```html
<!DOCTYPE html>
<html lang="en">
<head>
<meta charset="utf-8">
<title>Orla Property Development – Business Card</title>
<link rel="stylesheet" href="https://fonts.googleapis.com/css2?family=Ubuntu:wght@300;400;700&display=swap">
<style>
  :root {
    --backdrop: #dfe1e1;
    --card-black: #151516;
    --card-edge: #2a2a2c;
    --ink-silver: #9c9ea2;
    --ink-light: #c9cbce;
    --perforation: #2c2d30;
    --perforation-fade: #151516;
  }
  * { margin: 0; padding: 0; box-sizing: border-box; }
  html, body {
    width: 1200px; height: 1000px; overflow: hidden;
    background: var(--backdrop);
  }
  .canvas {
    position: relative; width: 1200px; height: 1000px;
    display: flex; align-items: center; justify-content: center;
  }
  .card {
    position: relative; width: 880px; height: 555px;
    background: var(--card-black);
    border: 1px solid var(--card-edge);
    border-radius: 28px;
    font-family: "Ubuntu", sans-serif;
    color: var(--ink-silver);
    overflow: hidden;
    box-shadow: 0 18px 40px rgba(0,0,0,0.25);
  }
  .brand {
    position: absolute; top: 62px; right: 60px;
    display: flex; align-items: center; gap: 18px;
  }
  .brand-mark {
    width: 54px; height: 54px; background: var(--ink-light);
  }
  .brand-name {
    font-size: 30px; font-weight: 400; color: var(--ink-light);
    letter-spacing: 0.5px;
  }
  .holder { position: absolute; left: 62px; top: 200px; }
  .holder-name { font-size: 36px; font-weight: 700; color: var(--ink-silver); }
  .holder-title { font-size: 20px; font-weight: 300; margin-top: 4px; }
  .contact {
    position: absolute; left: 62px; top: 300px;
    font-size: 21px; font-weight: 300; line-height: 28px; color: var(--ink-light);
  }
  .contact .email { margin-top: 18px; }
  .perforated-band {
    position: absolute; left: 260px; right: 30px; top: 412px; height: 52px;
    background: linear-gradient(90deg, var(--perforation-fade), var(--perforation) 35%, var(--perforation) 80%, var(--perforation-fade));
  }
  .perforated-band.lower { left: 30px; top: 508px; height: 22px; }
  .website {
    position: absolute; right: 60px; top: 372px;
    font-size: 21px; font-weight: 300; color: var(--ink-light);
  }
  .address {
    position: absolute; left: 62px; top: 474px;
    font-size: 21px; font-weight: 300; color: var(--ink-light);
  }
</style>
</head>
<body>
<main class="canvas">
  <article class="card">
    <header class="brand">
      <span class="brand-mark"></span>
      <span class="brand-name">Orla Property Development</span>
    </header>

    <section class="holder">
      <h1 class="holder-name">Darren Ashcombe</h1>
      <p class="holder-title">Managing Director</p>
    </section>

    <section class="contact">
      <p>+61 438 615 207</p>
      <p>+61 3 8276 4139</p>
      <p class="email">darren@orla.properties</p>
    </section>

    <p class="website">www.orla.properties</p>

    <div class="perforated-band" role="img" aria-label="Band of perforated cut-out dots through the metal card"></div>
    <p class="address">PO Box 73, Marrowfield, VIC 3291</p>
    <div class="perforated-band lower" role="img" aria-label="Narrow strip of perforated cut-out dots along the lower edge"></div>
  </article>
</main>
</body>
</html>
```